Volunteer fire fighters needed banner

As part of our recruitment campaign, we need a sign we can post on our sign trailer to entice locals to join our volunteer fire service. This design will be printed on a banner, front and back, to catch traffic going in both directions on a busy roadway. This banner will have a printed surface of 4 feet tall by 8 feet long.
Our fire department is looking to attract people between the ages of 18 and 35 years old who are interested in being a firefighter. We offer our volunteers:
-Free professional training
-All equipment supplied
-Tax abatements for active volunteers
For more information, you can check us out at:
Brookmerecrestfire.example

This design should:
-scale to and fit a 4'x8' canvas
-Include our web address "BrookmereCrestFire.example"
-Say "Members Wanted"
-"Drill every Tuesday at 7pm"
-"37 Quarry Bend Lane"
-Include "Brookmere Crest Fire Department"

We've included reference photos and past images we use for our other campaigns for inspiration for you.

Target Market(s)

18-35 y/o

Industry/Entity Type

Fire Service

Requirements
Must have
• -scale to and fit a 4'x8' canvas -Include our web address "BrookmereCrestFire.example" -Say "Members Wanted" -"Drill every Tuesday at 7pm" -"37 Quarry Bend Lane" -Include "Brookmere Crest Fire Department"

```html
<!DOCTYPE html>
<html lang="en">
<head>
<meta charset="utf-8">
<title>Brookmere Crest Fire Department – Members Wanted</title>
<link rel="stylesheet" href="https://fonts.googleapis.com/css2?family=Anton&family=Oswald:wght@400;500&family=Pathway+Gothic+One&family=Montserrat:wght@700&display=swap">
<style>
  :root {
    --fire-red: #ae1f24;
    --signal-yellow: #fbb321;
    --ink: #1b1b1b;
    --navy: #2f3f72;
    --white: #ffffff;
    --photo-truck: linear-gradient(135deg, #9a9b98 0%, #c8c9c4 35%, #b8272a 60%, #7c1a1c 100%);
    --photo-night: linear-gradient(160deg, #2d3f63 0%, #3d5c56 50%, #3a4a2a 100%);
    --art-hero: linear-gradient(150deg, #c9d2df 0%, #6e7787 40%, #2f3440 65%, #e06a25 100%);
  }
  * { margin: 0; padding: 0; box-sizing: border-box; }
  html, body { width: 1200px; height: 600px; overflow: hidden; background: #ffffff; }
  .banner { position: relative; width: 1200px; height: 600px; background: var(--fire-red); overflow: hidden; }

  .photo { position: absolute; left: 812px; width: 388px; }
  .photo-truck { top: 0; height: 295px; background: var(--photo-truck); }
  .photo-night { top: 299px; height: 301px; background: var(--photo-night); }

  .title-band { position: absolute; left: 0; top: 0; width: 905px; height: 95px; background: var(--signal-yellow);
    clip-path: polygon(0 0, 100% 0, 90% 100%, 0 100%); }
  .dept-name { position: absolute; left: 40px; top: 18px; font-family: "Anton", sans-serif; font-weight: 400; font-size: 55px;
    line-height: 1; color: var(--ink); text-transform: uppercase; white-space: nowrap; }

  .headline-box { position: absolute; left: 38px; top: 128px; width: 460px; height: 104px;
    border: 8px solid var(--white); display: flex; align-items: center; justify-content: center; }
  .headline { font-family: "Oswald", sans-serif; font-weight: 500; font-size: 54px; color: var(--white);
    text-transform: uppercase; line-height: 1; white-space: nowrap; }

  .drill-info { position: absolute; left: 530px; top: 150px; font-family: "Oswald", sans-serif; font-weight: 400;
    font-size: 25px; line-height: 34px; color: var(--signal-yellow); white-space: nowrap; }

  .hero-art { position: absolute; left: 500px; top: 238px; width: 312px; height: 268px; background: var(--art-hero); }

  .offer-title { position: absolute; left: 58px; top: 280px; font-family: "Oswald", sans-serif; font-weight: 500;
    font-size: 29px; line-height: 40px; color: var(--signal-yellow); text-transform: uppercase; white-space: nowrap; }
  .offer-list { position: absolute; left: 58px; top: 322px; width: 345px; list-style: none;
    font-family: "Pathway Gothic One", sans-serif; font-size: 39px; line-height: 40px; color: var(--white); }
  .offer-list li { padding-left: 16px; text-indent: -16px; }

  .info-strip { position: absolute; left: 0; top: 500px; width: 860px; height: 30px; background: var(--signal-yellow);
    clip-path: polygon(0 0, 100% 0, 97% 100%, 0 100%); }
  .info-label { position: absolute; left: 58px; top: 502px; font-family: "Oswald", sans-serif; font-weight: 500;
    font-size: 21px; line-height: 26px; color: var(--ink); white-space: nowrap; }

  .url-band { position: absolute; left: 0; top: 530px; width: 1200px; height: 70px; background: var(--navy); }
  .web-address { position: absolute; left: 58px; top: 536px; font-family: "Montserrat", sans-serif; font-weight: 700;
    font-size: 46px; line-height: 58px; color: var(--white); letter-spacing: 1px; white-space: nowrap; }

  .crest-mark { position: absolute; left: 900px; top: 500px; display: flex; align-items: center; gap: 12px; }
  .crest-dot { width: 60px; height: 60px; border-radius: 50%; background: var(--fire-red); border: 3px solid var(--signal-yellow); flex: none; }
  .crest-name { font-family: "Oswald", sans-serif; font-weight: 500; font-size: 26px; color: var(--white);
    text-transform: uppercase; white-space: nowrap; }
</style>
</head>
<body>
<main class="banner">
  <div class="photo photo-truck" role="img" aria-label="Photo of a red fire engine parked inside the station bay"></div>
  <div class="photo photo-night" role="img" aria-label="Photo of volunteers laying supply hose from an engine at dusk"></div>

  <div class="title-band"></div>
  <h1 class="dept-name">Brookmere Crest Fire Department</h1>

  <div class="headline-box"><h2 class="headline">Members Wanted</h2></div>

  <p class="drill-info">Drill every Tuesday at 7pm<br>37 Quarry Bend Lane</p>

  <div class="hero-art" role="img" aria-label="Illustration of a firefighter in breathing gear spraying a hose in front of a flag and flames"></div>

  <h3 class="offer-title">We offer our volunteers:</h3>
  <ul class="offer-list">
    <li>-Free professional training</li>
    <li>-All equipment supplied</li>
    <li>-Tax abatements for active volunteers</li>
  </ul>

  <div class="info-strip"></div>
  <p class="info-label">For more information, you can check us out at:</p>

  <div class="url-band"></div>
  <p class="web-address">BrookmereCrestFire.example</p>

  <div class="crest-mark">
    <span class="crest-dot"></span>
    <span class="crest-name">Brookmere Crest</span>
  </div>
</main>
</body>
</html>
```